dessert restaurant

I need a business card design for my restaurant. It will primarily be a dessert and wine restaurant. I will serve delicious baked from scratch desserts, cake, pies cookies brownies etc. Select red and white wines.I will also offer light breakfast, and lunch menu. This will be an upscale contemporary design restaurant with reasonably priced items on the menu. I will also offer small plates in the evening with dessert menu. my color scheme is cobalt blue , red, white black. My restaurant will be the place where adults come after enjoying the meal at a restaurant and want to enjoy a dessert and a glass of wine to finish off their evening. I will also have contemporary jazz sounds for atmosphere.

Industry/Entity Type

Restaurant

Contact Information for Business Card

tessa marlowe 415 555 0193

```html
<!DOCTYPE html>
<html lang="en">
<head>
<meta charset="utf-8">
<title>Velvetine — Business Card</title>
<link rel="stylesheet" href="https://fonts.googleapis.com/css2?family=Ropa+Sans&display=swap">
<style>
  :root {
    --page: #ffffff;
    --card: #2e222d;
    --cream: #ecd3aa;
    --red: #d9574a;
    --green: #a7b85b;
    --plaid-dark: #3a2c33;
    --plaid-mid: #6b5a4a;
  }
  * { margin: 0; padding: 0; box-sizing: border-box; }
  html, body {
    width: 1200px; height: 1000px; overflow: hidden;
    background: var(--page);
    font-family: "Ropa Sans", Arial, sans-serif;
  }
  .card {
    position: absolute; left: 283px; top: 315px;
    width: 634px; height: 370px;
    background: var(--card);
    box-shadow: 0 3px 8px rgba(0,0,0,0.18);
    overflow: hidden;
  }
  .plaid-band {
    position: absolute; left: 0; top: 0; width: 100%; height: 76px;
    background: linear-gradient(180deg, var(--plaid-mid), var(--plaid-dark) 50%, var(--plaid-mid));
  }
  .band-rule {
    position: absolute; left: 0; top: 76px; width: 100%; height: 4px;
    background: var(--cream);
  }
  .brand-mark {
    position: absolute; left: 80px; top: 60px; width: 114px; height: 114px;
    border-radius: 50%;
    background: var(--card);
    border: 2px solid var(--cream);
  }
  .brand-name {
    position: absolute; left: 224px; top: 86px;
    font-size: 56px; line-height: 1; letter-spacing: 7px;
    color: var(--cream);
  }
  .contact { position: absolute; left: 80px; top: 214px; color: var(--cream); }
  .contact-name {
    font-size: 27px; letter-spacing: 2.5px; color: var(--red);
    text-transform: uppercase; margin-bottom: 14px;
  }
  .contact-address { font-size: 15px; line-height: 20px; }
  .contact-phone {
    display: flex; align-items: center; gap: 7px;
    font-size: 15px; margin-top: 15px;
  }
  .contact-phone svg { width: 15px; height: 13px; fill: var(--cream); }
  .hours { position: absolute; left: 400px; top: 213px; color: var(--cream); }
  .hours-title {
    font-size: 16px; color: var(--green); text-transform: uppercase; line-height: 18px;
  }
  .hours-table { border-collapse: collapse; font-size: 15px; }
  .hours-table td { padding: 0; line-height: 19.5px; vertical-align: top; }
  .hours-table .day { width: 80px; }
</style>
</head>
<body>
  <article class="card">
    <div class="plaid-band" role="img" aria-label="Plaid pattern band in cream, red and green"></div>
    <div class="band-rule"></div>
    <div class="brand-mark"></div>
    <h1 class="brand-name">VELVETINE</h1>

    <section class="contact">
      <h2 class="contact-name">Tessa Marlowe</h2>
      <p class="contact-address">1187 Alder Row, N.W.<br>Washington, D.C. 20011</p>
      <p class="contact-phone">
        <svg viewBox="0 0 16 14" aria-hidden="true">
          <path d="M1 4 C1 1.5 4 1 8 1 C12 1 15 1.5 15 4 L15 5 L11.5 5 L11.5 3.5 L4.5 3.5 L4.5 5 L1 5 Z"/>
          <path d="M4 6 L12 6 L14 13 L2 13 Z"/>
        </svg>
        +1 415 555 0193
      </p>
    </section>

    <section class="hours">
      <h3 class="hours-title">Opening Hours</h3>
      <table class="hours-table">
        <tr><td class="day">Mon - Wed</td><td>8am - 2pm</td></tr>
        <tr><td class="day">Thu</td><td>8am - 2pm<br>4pm - 10pm</td></tr>
        <tr><td class="day">Fri - Sat</td><td>8am - 2pm</td></tr>
        <tr><td class="day">Sun</td><td>Closed</td></tr>
      </table>
    </section>
  </article>
</body>
</html>
```